International Property Consultancy

Detailed Wireframe and info document attached.

Brief Overview:

I need a dynamic and well designed website that is easy to use and understand. It has to be unique and different to generic templates that most websites seem to be these days. PLEASE NO GENERIC TEMPLATES FROM THE INTERNET.

Our business has 10 years experience working on struggling international developments that we then work in-house for to turn around and brings bout success. We stay within a project often for long periods of time until success is achieved. We are unique in our approach and completely different to the standard routes to market for many developments. The site is for developers to see what we have done in regards to previous projects, as such we want to incorporate video into this site with a strong design aesthetic. There will be videos of the past projects we have worked on, which will act as case studies.

I like very simple but punchy websites, that people can navigate and understand very easily. Also a big fan of unique and well thought out design aesthetic.

Initial Site layout thoughts:

1) Homepage:
2) About Us
3) What we've done / Work
This part has the projects we have worked on (France, Portugal, London, Morocco). Each one will have some video content and photo images, but also would be good to have a succinct way to mention what we did and the successes in a clever and punchy way.

4) Contact Us

* This is just a guideline. Would be open to input and creative direction on your own part.

*More details and websites we like can be seen in the brief doc attached.

PLEASE VIEW THE WIREFRAME WORD DOC ATTACHED.

Here there are also some more examples to help:

Here are just a few examples of websites and what I like about them:

- www.velmorit.com (clean, nice geometric design aesthetic, good animation when loading and changing pages well thought out all though also coulee be considered a bit dull and basic after the initial homepage slide)
- https://www.farbridgeloop.net (Clean site, quite clinical, lacks video content and doesn't engage greatly).
- https://quiltmarsh.com (minimal, and like how it mixes the design aesthetic more with video and photo content)

- https://www.theamberotter.com (like the layout of this and how it displays the projects and work section)

- https://drov.com (Good use of video content)

- https://crafthalo.studio (minimal to the point and mixes design with video and animation etc...)

Here is another couple of cool websites that may help give you some direction: https://tidewellgroup.com www.drov.com

Hi there, One of the things I thought would be good on the homepage is to add the logo with a 'digital landscape' before flicking down into a slide with video content of the projects... Just an idea but have posted some pics in the brief. We would get this animated for the site. But if you have better ideas, please do run with them. Thanks,

Target Market(s)

Property developers

Number of Pages Required

4 page

Font styles to use
Other font styles liked:
• Read brief

Requirements
Must have
• Needs to be clean, dynamic and easy to follow on desktop and mobile. We will use it as a kind of portfolio website so will need to embed video of past projects we have worked on.

Read brief in docs.
Nice to have
• Clean
Should not have
• Not be another generic template website.
Not have random property stock photos. (We are not a property agency).

```html
<!DOCTYPE html>
<html lang="en">
<head>
<meta charset="utf-8">
<title>Calvenor — International Property Developments</title>
<link href="https://fonts.googleapis.com/css2?family=Figtree:wght@300;400;600;700;800&display=swap" rel="stylesheet">
<style>
  :root{
    --teal-deep:#11465a;
    --teal-footer:#0f4558;
    --navy:#1d3553;
    --ink:#12485b;
    --cream:#f6f5ef;
    --white:#ffffff;
    --line-soft:#b7c6cc;
    --nav-grey:#2b3f55;
    --photo-a:#1d5a70;
    --photo-b:#2e7690;
    --photo-c:#173f55;
  }
  *{margin:0;padding:0;box-sizing:border-box}
  html,body{width:668px;height:1200px;overflow:hidden}
  body{font-family:"Figtree",Arial,sans-serif;background:var(--white);color:var(--navy);position:relative}

  .site-header{position:absolute;top:0;left:0;width:668px;height:60px}
  .brand{position:absolute;left:55px;top:16px;font-size:22px;font-weight:700;letter-spacing:0.5px;color:var(--navy);line-height:1}
  .main-nav{position:absolute;top:22px;left:311px;display:flex;gap:0}
  .main-nav a{font-size:8px;text-decoration:none;color:var(--nav-grey);font-weight:300;letter-spacing:0.2px;margin-right:34px;white-space:nowrap}
  .main-nav a.is-active{font-weight:700;color:var(--navy)}

  .hero{position:absolute;top:60px;left:0;width:668px;height:373px}
  .hero-deco{position:absolute;right:0;top:50px}
  .hero-title{position:absolute;left:54px;top:105px;font-size:45px;font-weight:800;color:var(--ink);letter-spacing:-0.3px;line-height:1}
  .hero-sub{position:absolute;left:58px;top:158px;font-size:21.5px;font-weight:700;color:var(--ink);line-height:1}
  .scroll-cue{position:absolute;left:313px;top:321px;width:40px;text-align:center;font-size:7.5px;color:var(--nav-grey);font-weight:400}
  .scroll-cue svg{display:block;margin:4px auto 0}

  .showcase{position:absolute;top:433px;left:0;width:668px;height:389px;background:var(--teal-deep)}
  .showcase-media{position:absolute;top:16px;left:0;width:668px;height:373px;background:linear-gradient(100deg,var(--photo-a) 0%,var(--photo-b) 45%,var(--photo-c) 70%,#2a6f94 100%)}
  .showcase-brand{position:absolute;left:63px;top:102px;display:flex;align-items:center;gap:10px;color:var(--white);font-size:23px;font-weight:400}
  .showcase-brand .dot{width:22px;height:22px;border-radius:50%;background:var(--white)}
  .showcase-title{position:absolute;left:60px;top:151px;font-size:25.5px;font-weight:700;color:var(--white);line-height:1.16}
  .stat-number{position:absolute;left:63px;top:232px;font-size:20px;font-weight:700;color:var(--white);line-height:1}
  .stat-label{position:absolute;left:63px;top:257px;font-size:13.5px;font-weight:700;color:var(--white);line-height:1}
  .play-button{position:absolute;left:468px;top:131px}
  .slider-dots{position:absolute;left:313px;top:360px;display:flex;gap:4px}
  .slider-dots span{width:7px;height:7px;border-radius:50%;border:1px solid var(--white)}
  .slider-dots span.is-current{background:var(--white)}

  .intro{position:absolute;top:822px;left:0;width:668px;height:285px;background:var(--cream);border-bottom:1px solid #d5d6d3}
  .intro-text{position:absolute;left:0;top:84px;width:668px;text-align:center;font-size:16px;font-weight:700;line-height:23px;color:var(--navy)}
  .btn-work{position:absolute;left:280px;top:166px;width:99px;height:25px;background:var(--teal-deep);color:var(--white);font-size:8px;font-weight:700;display:flex;align-items:center;justify-content:center;gap:3px;text-decoration:none}

  .site-footer{position:absolute;top:1108px;left:0;width:668px;height:92px;background:var(--teal-footer);color:var(--white)}
  .footer-brand{position:absolute;left:63px;top:19px;font-size:20px;font-weight:700;letter-spacing:0.5px;line-height:1}
  .footer-nav{position:absolute;left:211px;top:26px;display:flex}
  .footer-nav a{color:var(--white);font-size:7px;font-weight:700;text-decoration:none;margin-right:24px;white-space:nowrap}
  .social{position:absolute;left:532px;top:20px;display:flex;gap:7.5px}
  .social span{width:16px;height:16px;border-radius:50%;background:var(--white)}
  .footer-rule{position:absolute;left:0;top:58px;width:655px;height:1px;background:rgba(255,255,255,0.18)}
  .copyright{position:absolute;left:63px;top:72px;font-size:7px;font-weight:300}
  .legal{position:absolute;left:507px;top:70px;font-size:6.5px;font-weight:300;white-space:nowrap}
</style>
</head>
<body>

<header class="site-header">
  <div class="brand">calvenor.</div>
  <nav class="main-nav">
    <a href="#" class="is-active">HOME</a>
    <a href="#">ABOUT US</a>
    <a href="#">WHAT WE'VE DONE</a>
    <a href="#">CONTACT US</a>
  </nav>
</header>

<section class="hero">
  <svg class="hero-deco" width="120" height="200" viewBox="0 0 120 200" aria-hidden="true">
    <circle cx="110" cy="60" r="56" fill="none" stroke="var(--line-soft)" stroke-width="1"/>
  </svg>
  <h1 class="hero-title">We are Calvenor</h1>
  <p class="hero-sub">We fulfill international property developments</p>
  <div class="scroll-cue">Scroll
    <svg width="10" height="16" viewBox="0 0 10 16" aria-hidden="true">
      <rect x="1" y="1" width="8" height="14" rx="4" fill="none" stroke="var(--navy)" stroke-width="1"/>
      <line x1="5" y1="4" x2="5" y2="7" stroke="var(--navy)" stroke-width="1"/>
    </svg>
  </div>
</section>

<section class="showcase">
  <div class="showcase-media" role="img" aria-label="Project video still: a team meeting around a table in a glass-walled office"></div>
  <div class="showcase-brand"><span class="dot"></span>Lumeris</div>
  <h2 class="showcase-title">Augiat in pede Fusce<br>tellus Sed metus</h2>
  <p class="stat-number">50 Project</p>
  <p class="stat-label">we delivered</p>
  <svg class="play-button" width="56" height="56" viewBox="0 0 56 56" aria-label="Play video" role="img">
    <circle cx="28" cy="28" r="27" fill="none" stroke="var(--white)" stroke-width="1.2"/>
    <path d="M19 17 L40 28 L19 39 Z" fill="none" stroke="var(--white)" stroke-width="1.2" stroke-linejoin="round"/>
  </svg>
  <div class="slider-dots"><span></span><span class="is-current"></span><span></span><span></span></div>
</section>

<section class="intro">
  <p class="intro-text">We deliver a unique and truly bespoke approach to<br>delivering international developments to market,<br>with over 10 years success around the world.</p>
  <a href="#" class="btn-work">See our Work
    <svg width="10" height="7" viewBox="0 0 10 7" aria-hidden="true"><path d="M0 3.5 H9 M6 0.5 L9 3.5 L6 6.5" fill="none" stroke="var(--white)" stroke-width="0.9"/></svg>
  </a>
</section>

<footer class="site-footer">
  <div class="footer-brand">calvenor.</div>
  <nav class="footer-nav">
    <a href="#">ABOUT US</a>
    <a href="#">WHAT WE'VE DONE</a>
    <a href="#">CONTACT US</a>
  </nav>
  <div class="social" aria-label="Social links"><span></span><span></span><span></span></div>
  <div class="footer-rule"></div>
  <p class="copyright">© 2020 calvenor. All Right Reserved</p>
  <p class="legal">Privacy Policy &nbsp;&nbsp;| &nbsp;&nbsp;Terms of Use</p>
</footer>

</body>
</html>
```